Website Design for Solar Panel Company

We are working with a company called BrightVX.

Some sites to use for content/competitors and inspiration:
https://www.dawnmill.com
https://prod.cdn-prod.raylokt.com
https://mossbeamvolt.net
https://www.quorvin.com/solarpanels

Thank you for taking the time to consider designing a website for us. We are web developers based in Stockton, CA, USA. Most of our projects go through the same process. Understanding this process may help you win a project with us. We custom-code all of our websites in-house. We don’t have any requirements as to what tools you use for your design, but we prefer Figma files. For any design that we label as four-stars, we send it to the client for review. The client picks the final design they want us to use. Once we complete this process, we will continue to show additional clients all the four-star sites and purchase them later. Your designs will have multiple chances to sell. For better chances of success, we ask that you follow these guidelines.

IMAGES:
If you use any images or icons in the design, we ask that you have a link to the asset so we can purchase the image/icon. Most of the designs we submit do not have the customer’s images on them unless they have some great images. Be creative; show us the feeling you are trying to portray with your image choices. Use any royalty-free site you choose. We subscribe to Corvane and mainly use their images, but we can purchase images outside of Corvane. PLEASE NOTE: we will not submit designs to clients with watermarks on the images.

FONTS:
We ask that you identify the fonts used in the design. This can be done in a message if you want. We typically use Tivelo Fonts and Corvane Fonts.

CONTENT:
We're always open to different content and ideas. We often submit designs with stock images so the client can see our vision. We typically take pictures after the website launch to use their images with our vision. Lorem Ipsum is fine for paragraphs, but we ask that you write the headers in correct English. We want to be able to show the vision and identify the sections of the website.

INSPIRATION:
We typically add a couple of links in the brief of websites we like to help you get started in your design.

REVISIONS:
We do not often ask for revisions of the designs unless we see something in the design that may not appeal to the client. If there are slight changes that we want to make, we do that in the development process.

FEEDBACK:
We rarely give feedback on designs during the design process. We are working on many website projects and do not have the time to provide feedback. We usually respond if your request is well thought out and asks specific questions, but a note asking “feedback, please” usually goes unanswered.

```html
<!DOCTYPE html>
<html lang="en">
<head>
<meta charset="utf-8">
<title>BrightVX — Solar Energy</title>
<link href="https://fonts.googleapis.com/css2?family=Jost:wght@400;500;600&family=Poppins:wght@600;700;800&display=swap" rel="stylesheet">
<style>
:root{
  --green:#3dae25;
  --green-light:#6fd63c;
  --green-soft:#5cbf4a;
  --ink:#1d1d1d;
  --body:#555;
  --grey-bg:#f5f5f5;
  --footer:#232323;
  --footer-text:#f2f2f2;
  --white:#fff;
}
*{margin:0;padding:0;box-sizing:border-box}
html,body{width:1200px;height:4240px;overflow:hidden}
body{position:relative;background:var(--white);font-family:'Jost',sans-serif;color:var(--ink)}
.abs{position:absolute}
.heading{font-family:'Poppins',sans-serif;font-weight:700;text-transform:uppercase;line-height:1.22}
.btn{position:absolute;display:flex;align-items:center;justify-content:center;background:var(--green);color:var(--white);font-family:'Jost',sans-serif;font-weight:500;text-transform:uppercase}
.photo{position:absolute}
.label{position:absolute;display:flex;align-items:center;gap:10px;color:var(--green);font-weight:600;font-size:22px;text-transform:uppercase}
.label::before{content:"";width:85px;height:3px;background:var(--green)}

/* top bar */
.topbar{left:0;top:0;width:1200px;height:38px;background:#111;color:var(--white);font-size:17px}
.topbar span{position:absolute;top:9px;display:flex;align-items:center;gap:8px}
/* nav */
.brand{font-family:'Poppins',sans-serif;font-weight:800;letter-spacing:1px}
.nav a{position:absolute;top:68px;font-size:17px;color:var(--ink);text-decoration:none;font-weight:500}
/* hero */
.hero{left:0;top:118px;width:1200px;height:603px;background:linear-gradient(160deg,#6d8797 0%,#324a55 35%,#2a3f3a 60%,#3f5e22 100%)}
.hero-title{left:0;width:1200px;top:300px;text-align:center;color:var(--white);font-size:80px}
.hero-text{left:0;width:1200px;top:444px;text-align:center;color:var(--white);font-size:19px;line-height:1.35}
/* about */
.about-text{left:594px;width:545px;font-size:13.5px;line-height:1.4;color:var(--body)}
.stat-num{font-family:'Poppins',sans-serif;font-weight:700;color:var(--green);font-size:56px;line-height:1}
.stat-cap{font-size:16px;line-height:1.2;color:#333}
/* consult */
.consult{left:0;top:1452px;width:1200px;height:182px;background:linear-gradient(90deg,#2f9a1d 0%,#48b52b 50%,#7bd645 100%)}
/* benefits */
.benefit h3{font-family:'Jost',sans-serif;font-weight:600;font-size:22px}
.benefit p{font-size:14px;line-height:1.35;color:var(--body);width:420px;margin-top:6px}
/* testimonial */
.panel-green{background:linear-gradient(160deg,rgba(96,196,78,.95),rgba(78,178,62,.92)),#4a9e3b}
.circle-line{position:absolute;border:3px solid var(--white);border-radius:50%;display:flex;align-items:center;justify-content:center}
.arrow-btn{position:absolute;width:49px;height:31px;background:var(--green-soft);display:flex;align-items:center;justify-content:center}
/* form */
.field{position:absolute;background:var(--white);font-size:10px;color:#666;padding:10px 13px}
/* blog */
.blog-cap{position:absolute;width:209px;text-align:center;font-size:14px;line-height:1.55;text-decoration:underline;color:#333}
/* footer */
.footer{left:0;top:3835px;width:1200px;height:405px;background:var(--footer)}
.foot-h{position:absolute;top:3912px;font-family:'Jost',sans-serif;font-size:23px;font-weight:400;text-transform:uppercase;color:var(--footer-text);line-height:1.2}
.foot-item{position:absolute;display:flex;align-items:center;gap:12px;font-size:16px;color:var(--footer-text);line-height:1.2;white-space:nowrap}
.foot-small{position:absolute;font-size:12.5px;color:#ddd}
</style>
</head>
<body>

<!-- Top bar -->
<div class="abs topbar">
  <span style="left:734px">
    <svg width="22" height="18" viewBox="0 0 22 18"><rect x="1" y="3" width="20" height="14" fill="#fff"/><path d="M1 3 L11 11 L21 3" stroke="#111" stroke-width="2" fill="none"/></svg>
    info@website.com
  </span>
  <span style="left:1000px">
    <svg width="16" height="16" viewBox="0 0 24 24"><path d="M6.6 10.8a15.1 15.1 0 0 0 6.6 6.6l2.2-2.2c.3-.3.7-.4 1-.2 1.1.4 2.3.6 3.6.6.6 0 1 .4 1 1V20c0 .6-.4 1-1 1A17 17 0 0 1 3 4c0-.6.4-1 1-1h3.5c.6 0 1 .4 1 1 0 1.3.2 2.5.6 3.6.1.3 0 .7-.2 1z" fill="#fff"/></svg>
    +123 456 7890
  </span>
</div>

<!-- Header -->
<div class="abs brand" style="left:41px;top:58px;font-size:30px;color:var(--ink)">BRIGHTVX</div>
<nav class="nav">
  <a style="left:329px">HOME</a>
  <a style="left:431px">ABOUT US</a>
  <a style="left:560px">SERVICES</a>
  <a style="left:696px">PRICES</a>
  <a style="left:798px">FAQS</a>
</nav>
<div class="btn" style="left:1011px;top:61px;width:131px;height:31px;font-size:16px">Contact Us</div>

<!-- Hero -->
<div class="abs hero" role="img" aria-label="Photo of rows of solar panels in a green field under a sunny sky"></div>
<h1 class="abs heading hero-title">BrightVX</h1>
<p class="abs hero-text">Lorem ipsum dolor sit amet, consectetur adipiscing elit, sed do eiusmod<br>tempor incididunt ut labore et dolore magna aliqua.</p>
<div class="btn" style="left:520px;top:537px;width:188px;height:42px;font-size:19px">Get a Quote</div>

<!-- About -->
<div class="photo" style="left:56px;top:813px;width:495px;height:552px;background:linear-gradient(150deg,#c9d3e0 0%,#4a5f86 35%,#24355c 70%,#1b2747 100%)" role="img" aria-label="Close-up photo of a large solar panel array"></div>
<div class="label" style="left:594px;top:825px">About</div>
<h2 class="abs heading" style="left:594px;top:868px;font-size:36px">BrightVX<br>Solar Energy</h2>
<p class="abs about-text" style="top:986px">Lorem ipsum dolor sit amet, consectetur adipiscing elit, sed do eiusmod tempor incididunt ut labore et doloremagna aliqua. Ut enim ad minim veniam, quis nostrud exercitation ullamco laboris nisi ut aliquip ex ea commodo consequat.</p>
<p class="abs about-text" style="top:1054px">Lorem ipsum dolor sit amet, consectetur adipiscing elit, sed do eiusmod tempor incididunt ut labore et doloremagna aliqua. Ut enim ad minim veniam, quis nostrud exercitation ullamco laboris nisi ut aliquip ex ea commodo consequat.</p>
<div class="btn" style="left:594px;top:1152px;width:176px;height:43px;font-size:19px">Get a Quote</div>

<div class="abs" style="left:612px;top:1240px">
  <div class="stat-num">24<span style="font-size:28px;vertical-align:top">/7</span></div>
  <div class="stat-cap">System<br>Monitoring</div>
</div>
<div class="abs" style="left:815px;top:1240px">
  <div class="stat-num">10+</div>
  <div class="stat-cap">Years of<br>Experience</div>
</div>
<div class="abs" style="left:1009px;top:1240px">
  <div class="stat-num">20<span style="font-size:16px;font-family:'Jost',sans-serif;font-weight:600;vertical-align:top;margin-left:8px">Years</span></div>
  <div class="stat-cap">Performance<br>Guarantee</div>
</div>

<!-- Consultation band -->
<div class="abs consult" role="img" aria-label="Green tinted photo of solar panels"></div>
<h2 class="abs heading" style="left:91px;top:1506px;font-size:36px;color:var(--white)">Do You Need a Consultation?</h2>
<p class="abs" style="left:94px;top:1563px;font-size:19px;color:var(--white)">Solar can give you lots of advantages, from which you will surely benefit.</p>
<div class="btn" style="left:866px;top:1518px;width:201px;height:49px;font-size:21px;background:#111">Get a Quote</div>

<!-- Products -->
<div class="label" style="left:67px;top:1784px">Products</div>
<h2 class="abs heading" style="left:67px;top:1818px;font-size:36px">Our Product<br>Benefits</h2>

<div class="abs benefit" style="left:74px;top:1935px">
  <svg class="abs" style="left:-2px;top:5px" width="54" height="54" viewBox="0 0 54 54" fill="none" stroke="#3dae25" stroke-width="2"><circle cx="27" cy="27" r="22"/><circle cx="27" cy="27" r="15"/><path d="M31 21c-1-2-7-2-8 1s8 3 8 7-7 3-9 1M27 16v22"/></svg>
  <div style="margin-left:63px"><h3>Benefit 1</h3><p>Lorem ipsum dolor sit amet, consectetur adipiscing elit, sed do eiusmod temporincididunt ut labore et doloremagna aliqua.</p></div>
</div>
<div class="abs benefit" style="left:74px;top:2031px">
  <svg class="abs" style="left:-2px;top:0" width="54" height="56" viewBox="0 0 54 56" fill="none" stroke="#3dae25" stroke-width="2"><circle cx="27" cy="9" r="4"/><path d="M27 1v2M19 9h2M33 9h2M21 3l2 2M33 3l-2 2"/><path d="M8 20h38l4 16H4z"/><path d="M6 28h42M20 20l-2 16M34 20l2 16M27 36v14M18 50h18"/></svg>
  <div style="margin-left:63px"><h3>Benefit 2</h3><p>Lorem ipsum dolor sit amet, consectetur adipiscing elit, sed do eiusmod temporincididunt ut labore et doloremagna aliqua.</p></div>
</div>
<div class="abs benefit" style="left:74px;top:2133px">
  <svg class="abs" style="left:0;top:0" width="50" height="54" viewBox="0 0 50 54" fill="none" stroke="#3dae25" stroke-width="2"><path d="M6 4h22l8 8v12M6 4v44h18"/><circle cx="30" cy="34" r="9"/><path d="M36 41l9 9"/></svg>
  <div style="margin-left:63px"><h3>Benefit 3</h3><p>Lorem ipsum dolor sit amet, consectetur adipiscing elit, sed do eiusmod temporincididunt ut labore et doloremagna aliqua.</p></div>
</div>

<div class="photo" style="left:737px;top:1781px;width:374px;height:388px;background:linear-gradient(180deg,#d9e6ee 0%,#9db4c8 50%,#6c8a74 100%)" role="img" aria-label="Photo of solar panels beside trees"></div>
<div class="photo" style="left:621px;top:1842px;width:375px;height:390px;background:linear-gradient(180deg,#2e86b8 0%,#6aaed3 45%,#7cb94a 80%,#4a8c2c 100%)" role="img" aria-label="Illustration of a robot carrying a solar panel through a meadow"></div>

<!-- Testimonial -->
<div class="abs panel-green" style="left:0;top:2357px;width:597px;height:425px" role="img" aria-label="Green tinted photo of a technician at a solar panel field"></div>
<div class="circle-line" style="left:252px;top:2433px;width:98px;height:98px">
  <svg width="44" height="36" viewBox="0 0 44 36" fill="none" stroke="#fff" stroke-width="3"><path d="M4 4h14v14l-6 14H6l5-12H4zM25 4h14v14l-6 14h-6l5-12h-7z"/></svg>
</div>
<p class="abs" style="left:0;width:597px;top:2553px;text-align:center;color:var(--white);font-size:23px;font-weight:500">we enjoy working</p>
<h2 class="abs heading" style="left:0;width:597px;top:2588px;text-align:center;color:var(--white);font-size:36px">What Client Says</h2>

<div class="abs" style="left:597px;top:2357px;width:603px;height:425px;background:var(--grey-bg)"></div>
<div class="abs" style="left:850px;top:2428px;width:98px;height:98px;border-radius:50%;background:radial-gradient(circle,#8a7a6a,#3b3530)" role="img" aria-label="Client portrait"></div>
<p class="abs" style="left:665px;width:468px;top:2555px;text-align:center;color:#888;font-size:17px;line-height:1.35">Lorem ipsum dolor sit amet, consectetur adipiscing elit, sed do eiusmod temporincididunt ut labore et doloremagna aliqua.</p>
<p class="abs" style="left:597px;width:603px;top:2641px;text-align:center;font-weight:600;font-size:18px;letter-spacing:.5px">NORA VELLING</p>
<div class="arrow-btn" style="left:848px;top:2693px"><svg width="14" height="18" viewBox="0 0 14 18"><path d="M11 2L4 9l7 7" stroke="#fff" stroke-width="2" fill="none"/></svg></div>
<div class="arrow-btn" style="left:907px;top:2693px"><svg width="14" height="18" viewBox="0 0 14 18"><path d="M3 2l7 7-7 7" stroke="#fff" stroke-width="2" fill="none"/></svg></div>

<!-- Contact -->
<div class="abs" style="left:0;top:2782px;width:597px;height:428px;background:var(--grey-bg)"></div>
<div class="field" style="left:44px;top:2907px;width:241px;height:30px">Your Name</div>
<div class="field" style="left:309px;top:2907px;width:239px;height:30px">Your Phone</div>
<div class="field" style="left:44px;top:2958px;width:241px;height:30px">Email Address</div>
<div class="field" style="left:309px;top:2958px;width:239px;height:30px">Select Service</div>
<div class="field" style="left:44px;top:3004px;width:504px;height:62px">Additional Message</div>
<div class="btn" style="left:44px;top:3086px;width:501px;height:37px;font-size:10px;font-weight:600;background:linear-gradient(90deg,#35a61f,#6fd63c)">Get a Free Quote Now</div>

<div class="abs panel-green" style="left:597px;top:2782px;width:603px;height:428px" role="img" aria-label="Green tinted photo of a technician installing solar panels"></div>
<div class="circle-line" style="left:850px;top:2864px;width:98px;height:98px">
  <svg width="50" height="50" viewBox="0 0 24 24"><path d="M6.6 10.8a15.1 15.1 0 0 0 6.6 6.6l2.2-2.2c.3-.3.7-.4 1-.2 1.1.4 2.3.6 3.6.6.6 0 1 .4 1 1V20c0 .6-.4 1-1 1A17 17 0 0 1 3 4c0-.6.4-1 1-1h3.5c.6 0 1 .4 1 1 0 1.3.2 2.5.6 3.6.1.3 0 .7-.2 1z" fill="#fff"/></svg>
</div>
<p class="abs" style="left:597px;width:603px;top:2983px;text-align:center;color:var(--white);font-size:23px;font-weight:500">Contact US Now</p>
<h2 class="abs heading" style="left:597px;width:603px;top:3018px;text-align:center;color:var(--white);font-size:36px">Get in Touch</h2>
<p class="abs" style="left:597px;width:603px;top:3080px;text-align:center;color:var(--white);font-size:33px">123-456-6789</p>

<!-- Blog -->
<div class="label" style="left:462px;top:3279px">Latest News</div>
<h2 class="abs heading" style="left:0;width:1190px;top:3320px;text-align:center;font-size:36px">Recent From Blog</h2>

<div class="photo" style="left:87px;top:3437px;width:209px;height:247px;border-radius:10px;background:linear-gradient(180deg,#2f88bb,#77b6d9 55%,#6fae44)" role="img" aria-label="Illustration of a robot carrying a solar panel"></div>
<div class="photo" style="left:359px;top:3437px;width:209px;height:247px;border-radius:10px;background:linear-gradient(160deg,#b6c6c0,#4c5d78 45%,#2d3a55)" role="img" aria-label="Photo of solar panels on a house roof"></div>
<div class="photo" style="left:630px;top:3437px;width:209px;height:247px;border-radius:10px;background:linear-gradient(160deg,#e9eef2,#8aa0b3 40%,#c86a2a 75%,#3a4a5c)" role="img" aria-label="Photo of two workers inspecting solar panels"></div>
<div class="photo" style="left:902px;top:3437px;width:209px;height:247px;border-radius:10px;background:linear-gradient(180deg,#5e9fe0,#9fc9ef 55%,#2a4a9a)" role="img" aria-label="Photo of solar panels under a blue sky"></div>

<p class="blog-cap" style="left:87px;top:3700px">Lorem ipsum dolor sit amet,<br>consectetur adipiscing elit.</p>
<p class="blog-cap" style="left:359px;top:3700px">Lorem ipsum dolor sit amet,<br>consectetur adipiscing elit.</p>
<p class="blog-cap" style="left:630px;top:3700px">Lorem ipsum dolor sit amet,<br>consectetur adipiscing elit.</p>
<p class="blog-cap" style="left:902px;top:3700px">Lorem ipsum dolor sit amet,<br>consectetur adipiscing elit.</p>

<!-- Footer -->
<footer class="abs footer"></footer>
<div class="abs brand" style="left:72px;top:3908px;font-size:40px;color:var(--white)">BRIGHTVX</div>
<p class="abs" style="left:72px;top:3985px;width:320px;font-size:11.5px;line-height:1.35;color:#ccc">Lorem ipsum dolor sit amet, consectetur adipiscing elit, sed do eiusmod temporincididunt ut labore et doloremagna aliqua.</p>
<div class="abs" style="left:72px;top:4054px;width:16px;height:16px;border-radius:50%;background:var(--white)"></div>
<div class="abs" style="left:124px;top:4054px;width:16px;height:16px;border-radius:50%;background:var(--white)"></div>
<div class="abs" style="left:176px;top:4054px;width:16px;height:16px;border-radius:50%;background:var(--white)"></div>

<h3 class="foot-h" style="left:436px">Quick Links</h3>
<div class="foot-item" style="left:436px;top:3962px"><svg width="20" height="22" viewBox="0 0 20 22" fill="none" stroke="#3dae25" stroke-width="2.4"><path d="M6 6a8 8 0 1 0 8 0M10 1v9"/></svg><span>Home</span></div>
<div class="foot-item" style="left:436px;top:4005px"><svg width="20" height="22" viewBox="0 0 20 22" fill="none" stroke="#3dae25" stroke-width="2.4"><path d="M6 6a8 8 0 1 0 8 0M10 1v9"/></svg><span>About</span></div>
<div class="foot-item" style="left:436px;top:4048px"><svg width="20" height="22" viewBox="0 0 20 22" fill="none" stroke="#3dae25" stroke-width="2.4"><path d="M6 6a8 8 0 1 0 8 0M10 1v9"/></svg><span>Products</span></div>
<div class="foot-item" style="left:436px;top:4091px"><svg width="20" height="22" viewBox="0 0 20 22" fill="none" stroke="#3dae25" stroke-width="2.4"><path d="M6 6a8 8 0 1 0 8 0M10 1v9"/></svg><span>Prices</span></div>

<h3 class="foot-h" style="left:657px">Opening Hours</h3>
<div class="foot-item" style="left:657px;top:3962px"><svg width="24" height="24" viewBox="0 0 24 24" fill="none" stroke="#3dae25" stroke-width="2"><circle cx="12" cy="12" r="10"/><path d="M12 6v6l4 2"/></svg><span>Mon - Fri&nbsp; 7am - 5pm</span></div>
<div class="foot-item" style="left:657px;top:4013px"><svg width="24" height="24" viewBox="0 0 24 24" fill="none" stroke="#3dae25" stroke-width="2"><circle cx="12" cy="12" r="10"/><path d="M12 6v6l4 2"/></svg><span>Saturday - Closed</span></div>
<div class="foot-item" style="left:657px;top:4064px"><svg width="24" height="24" viewBox="0 0 24 24" fill="none" stroke="#3dae25" stroke-width="2"><circle cx="12" cy="12" r="10"/><path d="M12 6v6l4 2"/></svg><span>Sunday - Closed</span></div>

<h3 class="foot-h" style="left:946px">Stay Updated</h3>
<div class="abs" style="left:946px;top:3962px;width:175px;height:33px;background:var(--white);color:#999;font-size:12px;display:flex;align-items:center;justify-content:center">EMAIL ADDRESS</div>
<div class="btn" style="left:946px;top:4020px;width:175px;height:33px;font-size:16px">Signup Now</div>

<p class="foot-small" style="left:69px;top:4206px">Copyright 2024 BrightVX. All Rights Reserved.</p>
<p class="foot-small" style="left:918px;top:4206px">Privacy Policy | Terms &amp; Conditions</p>

</body>
</html>
```